Ridgeway Teen Circle (Flyer)

I want a flyer to advertise my service.
Details below, and logo's to use are attached.

A girls only after school program, 11-14yrs, as OSHC is no longer avail, dedicated to coaching & mentoring our girls into strong, independent young women.

The Brainchild of Rebecca Tolland, Ridgeway Teen Circle was created to address the growing demand for after school/school holiday supervision for kids moving from primary into high school, when OSHC ceases to exist.
With over 12 years experience mentoring and coaching young women in the corporate world, Bec decided to leave her role as a Director with Corlana Bank, and follow her passion.
Bec, along with her sister Jocelyn, who has over 10 years experience in local communities as a Youth Worker, and is also a qualified Enrolled Nurse, embarked on building a program designed to keep parents happy (by knowing their girls are safe) and dedicated to coaching and mentoring our girls into strong, independent young women.
Open every afternoon and during school holidays, we look to offer;
- Daily meditation
- Healthy snacks
- Dedicated homework time
- Organised group activity, led by qualified instructors (yoga, fitness class, soccer etc)
- Regular guests speakers, addressing issues/concerns for young people today
- SOCIAL MEDIA FREE ZONE

Located 317 Pembury Rd, Baulkham Hills (across from Ardmore Private Hospital)
Open 3-6pm Monday to Friday

Facebook page: http://fb.me/ridgewayteencircle
Email: info@ridgewayteencircle.example.com.au
Mobile: 0400555183

Target Market(s)

Parents of teenage girls, teenage girls 11-14 years

Industry/Entity Type

School

Font styles to use
Sans Serif

Colors
b768aa
e667a6

Requirements
Must have
• What progam is - see brief
• Who runs it
Should not have
• Not be too busy, not overly mature images

```html
<!DOCTYPE html>
<html lang="en">
<head>
<meta charset="utf-8">
<title>Ridgeway Teen Circle – Flyer</title>
<link href="https://fonts.googleapis.com/css2?family=Arimo:wght@400;700&display=swap" rel="stylesheet">
<style>
:root{
  --bg:#141414;
  --magenta:#e6199a;
  --pink:#e667a6;
  --purple:#b768aa;
  --deep-purple:#9b4fc0;
  --paper:#fbf4fa;
  --blush:#f1d3ea;
  --ink-dark:#25253a;
}
*{margin:0;padding:0;box-sizing:border-box}
html,body{width:1200px;height:1040px;overflow:hidden;background:var(--bg)}
body{font-family:"Arimo",Arial,sans-serif;position:relative}
.flyer{
  position:absolute;left:260px;top:20px;width:680px;height:1000px;
  background:linear-gradient(180deg,var(--blush) 0%,var(--paper) 22%,#fff 60%,var(--paper) 100%);
  overflow:hidden;
}
.headline{position:absolute;left:36px;top:34px;right:36px}
.headline__main{font-weight:700;font-size:86px;letter-spacing:-2px;color:var(--magenta);line-height:1}
.headline__sub{font-weight:400;font-size:46px;color:var(--purple);line-height:1.05;letter-spacing:-.5px}
.rule{position:absolute;left:36px;right:36px;height:2px;background:var(--purple)}
.rule--top{top:170px}
.rule--bottom{top:246px}
.intro{position:absolute;left:36px;right:36px;top:180px;font-size:22px;line-height:1.4;color:var(--magenta);text-align:center}
.brush-band{position:absolute;left:0;top:258px;width:680px;height:350px}
.about{position:absolute;left:40px;right:40px;top:278px;font-size:14.5px;line-height:1.55;color:var(--magenta);text-align:center}
.about p{margin-bottom:8px}
.dots{position:absolute;left:360px;top:620px;width:280px;height:180px;border-radius:50%;background:radial-gradient(circle,rgba(183,104,170,.13),rgba(183,104,170,0) 70%)}
.offer-tab{position:absolute;left:0;top:606px;width:290px;height:36px;background:var(--purple);color:#fff;font-size:22px;padding:5px 0 0 40px;clip-path:polygon(0 0,100% 0,92% 100%,0 100%)}
.offer-list{position:absolute;left:40px;right:30px;top:648px;list-style:none;font-size:20px;line-height:1.28;color:var(--magenta)}
.offer-list li{padding-left:26px;position:relative}
.offer-list li::before{content:"";position:absolute;left:2px;top:8px;width:10px;height:10px;border-radius:50%;background:var(--pink)}
.offer-list .cont::before{display:none}
.brand{position:absolute;right:26px;top:812px;font-size:17px;font-weight:700;color:var(--magenta);text-align:right;line-height:1.15}
.location{position:absolute;left:0;top:864px;width:680px;height:54px;background:linear-gradient(90deg,var(--purple),var(--deep-purple));color:#fff;font-size:16px;line-height:1.4;text-align:center;padding-top:5px}
.contact{position:absolute;left:0;right:0;top:924px;text-align:center;color:var(--magenta);font-size:17px;line-height:1.3}
.contact__fb::before{content:"";display:inline-block;width:14px;height:14px;background:var(--purple);margin-right:8px;vertical-align:-2px}
</style>
</head>
<body>
<main class="flyer">
  <header class="headline">
    <h1 class="headline__main">A GIRLS ONLY</h1>
    <h2 class="headline__sub">AFTER SCHOOL PROGRAM</h2>
  </header>
  <div class="rule rule--top"></div>
  <p class="intro">11-14yrs, as OSHC is no longer avail, dedicated to coaching &amp; mentoring our girls into strong, independent young women.</p>
  <div class="rule rule--bottom"></div>

  <svg class="brush-band" role="img" aria-label="Dark painted brush stroke band fading from grey to navy" viewBox="0 0 680 350">
    <defs>
      <linearGradient id="band" x1="0" y1="0" x2="1" y2="0.3">
        <stop offset="0" stop-color="#b9b4bc"/>
        <stop offset=".55" stop-color="#6c6a78"/>
        <stop offset="1" stop-color="#25253a"/>
      </linearGradient>
    </defs>
    <path d="M0 0H680V250C600 262 560 300 500 292C440 286 420 330 360 330C300 332 260 346 0 350Z" fill="url(#band)" opacity=".9"/>
  </svg>

  <section class="about">
    <p>The Brainchild of Rebecca Tolland, Ridgeway Teen Circle was created to address the growing demand for after school/school holiday supervision for kids moving from primary into high school, when OSHC ceases to exist.</p>
    <p>With over 12 years experience mentoring and coaching young women in the corporate world, Bec decided to leave her role as a Director with Corlana Bank, and follow her passion.</p>
    <p>Bec, along with her sister Jocelyn, who has over 10 years experience in local communities as a Youth Worker, and is also a qualified Enrolled Nurse, embarked on building a program designed to keep parents happy (by knowing their girls are safe) and dedicated to coaching and mentoring our girls into strong, independent young women.</p>
    <p>Open every afternoon and during school holidays</p>
  </section>

  <div class="dots" role="img" aria-label="Soft halftone dot decoration"></div>

  <div class="offer-tab">we look to offer :</div>
  <ul class="offer-list">
    <li>Daily meditation</li>
    <li>Healthy snacks</li>
    <li>Dedicated homework time</li>
    <li>Organised group activity, led by qualified instructors</li>
    <li class="cont">(yoga, fitness class, soccer etc)</li>
    <li>Regular guests speakers, addressing issues/concerns for</li>
    <li class="cont">young people today</li>
    <li>SOCIAL MEDIA FREE ZONE</li>
  </ul>

  <div class="brand">Ridgeway<br>Teen Circle</div>

  <section class="location">
    Located 317 Pembury Rd, Baulkham Hills (across from Ardmore Private Hospital)<br>
    Open 3-6pm Monday to Friday
  </section>

  <section class="contact">
    <p>Email: info@ridgewayteencircle.example.com.au</p>
    <p>Mobile: 0400555183</p>
    <p class="contact__fb">http://fb.me/ridgewayteencircle</p>
  </section>
</main>
</body>
</html>
```